Online Psychology Practice needs business cards.

Online Psychology service needs business cards. Have own logo- please see uploaded. I have other file formats if you need (not sure one needed?)

Details for Business Card:
Helena Marchetti
Clinical Psychologist BPsych, BPsych (Hons), MPsych (Clin), MAPS
T: 0439627015 | F: 08 73615204
E: hello@brightwatertelehealthcounselling.com.au
W: brightwatertelehealthcounselling.com.au

Industry/Entity Type

Health

Contact Information for Business Card

Logo plus details above (couldn't write in this section)

```html
<!DOCTYPE html>
<html lang="en">
<head>
<meta charset="utf-8">
<title>Brightwater Telehealth Counselling — Business Card</title>
<link href="https://fonts.googleapis.com/css2?family=Roboto+Condensed:wght@400;700&display=swap" rel="stylesheet">
<style>
  :root {
    --backdrop: #d9d4cc;
    --card-blue: #155a85;
    --card-blue-deep: #114b70;
    --navy: #163f66;
    --teal: #1a8fab;
    --text: #3c3c3c;
    --white: #ffffff;
  }
  * { margin: 0; padding: 0; box-sizing: border-box; }
  html, body {
    width: 1200px; height: 900px; overflow: hidden;
    background: var(--backdrop);
    font-family: "Roboto Condensed", sans-serif;
  }
  .canvas { position: relative; width: 1200px; height: 900px; }

  .card {
    position: absolute; left: 311px; width: 578px;
    box-shadow: 0 4px 12px rgba(0,0,0,0.18);
    overflow: hidden;
  }
  .card-front { top: 85px; height: 343px; background: var(--card-blue); }
  .card-back  { top: 472px; height: 329px; background: var(--white); }

  .front-brand {
    position: absolute; left: 0; right: 0; top: 96px;
    display: flex; flex-direction: column; align-items: center; gap: 18px;
  }
  .front-brand .brand-dot {
    width: 70px; height: 70px; border-radius: 50%;
    background: var(--card-blue-deep);
  }
  .front-brand .brand-name {
    color: var(--card-blue-deep);
    font-weight: 700; font-size: 30px; line-height: 1.05;
    text-align: center; letter-spacing: 3px; text-transform: uppercase;
  }

  .back-brand {
    position: absolute; left: 24px; top: 96px; width: 190px;
    display: flex; flex-direction: column; align-items: center; gap: 12px;
  }
  .back-brand .brand-dot {
    width: 56px; height: 56px; border-radius: 50%; background: var(--teal);
  }
  .back-brand .brand-name {
    color: var(--navy); font-weight: 700; font-size: 21px; line-height: 1.1;
    text-align: center; letter-spacing: 2px; text-transform: uppercase;
  }

  .divider {
    position: absolute; left: 235px; top: 87px; width: 2px; height: 155px;
    background: var(--navy);
  }

  .details { position: absolute; left: 255px; top: 86px; color: var(--text); }
  .details .person-name {
    color: var(--navy); font-weight: 700; font-size: 22px; letter-spacing: 0.3px;
    text-transform: uppercase; line-height: 1.1;
  }
  .details .role, .details .credentials { font-size: 14px; line-height: 21px; }
  .details .role { margin-top: 4px; }
  .contact-list { list-style: none; margin-top: 15px; }
  .contact-list li {
    display: flex; align-items: center; gap: 6px;
    font-size: 14px; line-height: 20.5px;
  }
  .contact-list svg { width: 13px; height: 13px; fill: var(--navy); flex: none; }

  .wave { position: absolute; left: 0; bottom: 0; width: 578px; height: 60px; }
</style>
</head>
<body>
<main class="canvas">

  <section class="card card-front" aria-label="Card front">
    <div class="front-brand">
      <span class="brand-dot"></span>
      <span class="brand-name">Brightwater<br>Telehealth Counselling</span>
    </div>
  </section>

  <section class="card card-back" aria-label="Card back">
    <div class="back-brand">
      <span class="brand-dot"></span>
      <span class="brand-name">Brightwater<br>Telehealth<br>Counselling</span>
    </div>

    <div class="divider"></div>

    <div class="details">
      <h1 class="person-name">Helena Marchetti</h1>
      <p class="role">Clinical Psychologist &amp; Principal Practitioner</p>
      <p class="credentials">BPsych, BPsych (Hons), MPsych (Clin), MAPS</p>
      <ul class="contact-list">
        <li>
          <svg viewBox="0 0 16 16"><path d="M3.6 1.2l2.3 2.6-1.3 1.9c.9 2 2.6 3.7 4.6 4.6l1.9-1.3 2.6 2.3-1.4 2.5C7 13.6 2.4 9 1.2 3.1z"/></svg>
          0439627015
        </li>
        <li>
          <svg viewBox="0 0 16 16"><path d="M4 1h8v4H4zM2 6h12a1 1 0 0 1 1 1v5h-3v3H4v-3H1V7a1 1 0 0 1 1-1zm3 5v3h6v-3z"/></svg>
          08 73615204
        </li>
        <li>
          <svg viewBox="0 0 16 16"><path d="M1 3h14v1.5L8 9 1 4.5zM1 6.2l7 4.4 7-4.4V13H1z"/></svg>
          hello@brightwatertelehealthcounselling.com.au
        </li>
        <li>
          <svg viewBox="0 0 16 16"><circle cx="8" cy="8" r="7"/><path d="M1 8h14M8 1c2.2 2 2.2 12 0 14M8 1c-2.2 2-2.2 12 0 14" stroke="#fff" stroke-width="1" fill="none"/></svg>
          brightwatertelehealthcounselling.com.au
        </li>
      </ul>
    </div>

    <svg class="wave" viewBox="0 0 578 60" preserveAspectRatio="none" aria-hidden="true">
      <path d="M0 28 C120 -6 260 10 360 22 C450 32 530 30 578 22 L578 60 L0 60 Z" fill="var(--teal)"/>
      <path d="M0 32 C130 8 260 20 360 30 C450 38 530 36 578 28 L578 60 L0 60 Z" fill="var(--white)"/>
      <path d="M0 36 C130 14 260 26 360 36 C450 44 530 42 578 34 L578 60 L0 60 Z" fill="var(--card-blue)"/>
    </svg>
  </section>

</main>
</body>
</html>
```